Business card for start up company

SIMPLE, CLEAN, FRESH, MODERN, SOPHISTICATED. professional. experienced, easy to deal with, expert in the field. local ethics.

professional business card for Forge Bay Industries. using company logo supplied and images.

GENERAL ENGINEERING - MACHINING - WELDING - MAINTENANCE

Forge Bay Industries Ltd is a locally owned mechanical engineering company that specialises in general and mechanical engineering, as well as steel fabrication, welding, repairs and maintenance.

We specialise in the design, welding, fabrication and installation of stainless and mild steel fabrications. We service commercial and residential clients; large or small projects; production line or one off designs.

We have built a solid reputation for quality and service for our machinery and engineering work around Northland NZ. For innovative, cost effective and efficient engineering solutions, to suit a wide range of commercial, residential and rural applications.

Target Market(s)

boat builders. DIY. industrial. RESIDENTIAL. COMMERCIAL

Industry/Entity Type

Mechanical Engineering

Contact Information for Business Card

CONTACT / SERVICES SIDE
Forge Bay Industries Ltd.
Design | Machining | Welding | Fabrication | Installation | Maintenance
www.forgebayindustries.example.nz
kevin@forgebayindustries.example.nz

Font styles to use
Serif

Colors

Designer to choose colors to be used in the design.

Requirements
Must have
• LOGO ONLY WITH NEGATIVE SPACE ON FRONT SIDE
• services and contact side , either use stock photos (supplied) as background or background supplied in logo photos.
Nice to have
• use the symbol icon in logo on contact/ services side, , enlarged, transparent and faded into the background with text over the top on the
• Design | Machining | Welding | Fabrication | Installation | Maintenance
• the above services to be subtle, along the bottom edge of the services side. can i also have another proof with eh above services featuring on the bottom edge of the LOGO FRONT side to see if the text looks better with or without.
Should not have
• crowded, busy, different fonts. different casing.
• use fonts in the logo files designer to make font decision.

```html
<!DOCTYPE html>
<html lang="en">
<head>
<meta charset="utf-8">
<title>Forge Bay Industries — Business Card</title>
<link href="https://fonts.googleapis.com/css2?family=Arimo:wght@400;700&family=Tinos&display=swap" rel="stylesheet">
<style>
  :root {
    --stage: #d9d6d1;
    --paper-light: #ffffff;
    --paper-shade: #e4e4e4;
    --band: #3c3d41;
    --accent: #e0651e;
    --ink-dark: #3a3b3f;
    --ink-mid: #5a5c60;
    --steel-deep: #141416;
    --steel-mid: #3a3b3e;
    --steel-light: #6c6d70;
    --white: #ffffff;
  }
  * { margin: 0; padding: 0; box-sizing: border-box; }
  html, body {
    width: 1200px; height: 780px; overflow: hidden;
    background: var(--stage);
  }
  .canvas {
    position: relative; width: 1200px; height: 780px;
  }
  .card {
    position: absolute; top: 235px;
    width: 540px; height: 310px;
    overflow: hidden;
    box-shadow: 0 8px 22px rgba(0,0,0,0.25);
  }

  /* Contact / services side */
  .card--contact {
    left: 30px;
    background: linear-gradient(135deg, var(--paper-light) 0%, var(--paper-shade) 100%);
  }
  .contact__band {
    position: absolute; left: 0; top: 0; bottom: 0; width: 92px;
    background: var(--band);
    border-right: 2px solid var(--accent);
  }
  .contact__faint-block {
    position: absolute; right: 30px; top: 20px;
    width: 170px; height: 170px;
    background: rgba(0,0,0,0.035);
  }
  .contact__brand {
    position: absolute; left: 64px; top: 38px;
    display: flex; align-items: center; gap: 14px;
  }
  .brand-square {
    width: 56px; height: 56px; background: var(--accent);
  }
  .brand-name {
    font-family: "Arimo", sans-serif; font-weight: 700;
    font-size: 27px; letter-spacing: 0.5px;
    color: var(--ink-mid);
  }
  .contact__details {
    position: absolute; left: 120px; top: 132px;
  }
  .company-name {
    font-family: "Arimo", sans-serif; font-weight: 700;
    font-size: 18px; color: var(--ink-dark); letter-spacing: 0.3px;
    margin-bottom: 12px;
  }
  .contact-line {
    display: flex; align-items: center; gap: 8px;
    font-family: "Tinos", serif; font-size: 13px; color: var(--ink-mid);
    margin-bottom: 5px;
  }
  .contact-icon { width: 14px; height: 14px; flex: none; }
  .services {
    font-family: "Tinos", serif; font-size: 13px;
  }
  .contact__services {
    position: absolute; left: 120px; bottom: 26px;
    color: var(--ink-mid);
  }

  /* Logo front side */
  .card--front {
    left: 630px;
  }
  .front__photo {
    position: absolute; inset: 0;
    background:
      radial-gradient(ellipse at 60% 55%, var(--steel-light) 0%, var(--steel-mid) 35%, transparent 70%),
      linear-gradient(140deg, var(--steel-mid) 0%, var(--steel-deep) 100%);
  }
  .front__brand {
    position: absolute; left: 0; right: 0; top: 104px;
    display: flex; justify-content: center; align-items: center; gap: 14px;
  }
  .front__brand .brand-square { width: 40px; height: 40px; }
  .front__brand .brand-name { color: var(--white); font-size: 30px; }
  .front__services {
    position: absolute; left: 0; right: 0; bottom: 20px;
    text-align: center; color: var(--white); opacity: 0.9;
  }
</style>
</head>
<body>
<main class="canvas">

  <section class="card card--contact" aria-label="Contact and services side">
    <div class="contact__band"></div>
    <div class="contact__faint-block"></div>
    <div class="contact__brand">
      <div class="brand-square"></div>
      <span class="brand-name">FORGE BAY INDUSTRIES</span>
    </div>
    <div class="contact__details">
      <p class="company-name">FORGE BAY INDUSTRIES LTD.</p>
      <p class="contact-line">
        <svg class="contact-icon" viewBox="0 0 14 14" aria-hidden="true">
          <circle cx="7" cy="7" r="6.5" fill="var(--accent)"/>
          <circle cx="7" cy="7" r="3.6" fill="none" stroke="#fff" stroke-width="1"/>
          <line x1="3.4" y1="7" x2="10.6" y2="7" stroke="#fff" stroke-width="1"/>
          <ellipse cx="7" cy="7" rx="1.5" ry="3.6" fill="none" stroke="#fff" stroke-width="1"/>
        </svg>
        www.forgebayindustries.example.nz
      </p>
      <p class="contact-line">
        <svg class="contact-icon" viewBox="0 0 14 14" aria-hidden="true">
          <circle cx="7" cy="7" r="6.5" fill="var(--accent)"/>
          <rect x="3.5" y="4.6" width="7" height="4.8" fill="none" stroke="#fff" stroke-width="1"/>
          <polyline points="3.5,4.6 7,7.4 10.5,4.6" fill="none" stroke="#fff" stroke-width="1"/>
        </svg>
        kevin@forgebayindustries.example.nz
      </p>
    </div>
    <p class="services contact__services">Design | Machining | Welding | Fabrication | Installation | Maintenance</p>
  </section>

  <section class="card card--front" aria-label="Logo front side">
    <div class="front__photo" role="img" aria-label="Dark close-up photograph of a machined steel gear and threaded shaft"></div>
    <div class="front__brand">
      <div class="brand-square"></div>
      <span class="brand-name">FORGE BAY INDUSTRIES</span>
    </div>
    <p class="services front__services">Design | Machining | Welding | Fabrication | Installation | Maintenance</p>
  </section>

</main>
</body>
</html>
```